Stationary design for boutique production house

We need a stationary design for our production house, 'Lorin Studios' based in Singapore. We produce microfilms as well as podcasts, talkshows and events. Our logo is a stylized icon of our director, who is also the executive producer and host of our programs, Lorin. Our main company colors are Red, Black and white. We would like a clean, minimalist design incorporating our existing company logo that conveys a sense of urbanism and elegance.

Logo and font files are attached. f

Target Market(s)

We focus on lifestyle media rather than entertainment.

Industry/Entity Type

Boutique

Font styles to use
Serif
Sans Serif

Colors
ec1f27
ffffff
000000

Requirements
Must have
• Our company logo and at least one of our company colors.
Nice to have
• Our address and contact information.
Should not have
• Changes made to the company logo (using only certain parts of it is fine though)

```html
<!DOCTYPE html>
<html lang="en">
<head>
<meta charset="utf-8">
<title>Lorin Studios – Business Cards</title>
<link href="https://fonts.googleapis.com/css2?family=Barlow:wght@300;400;500&display=swap" rel="stylesheet">
<style>
  :root {
    --backdrop: #8e8f8e;
    --card-white: #ececee;
    --card-black: #262626;
    --brand-red: #ec1f27;
    --ink: #111111;
    --light-text: #e6e6e6;
  }
  html, body {
    margin: 0;
    padding: 0;
    width: 1200px;
    height: 900px;
    overflow: hidden;
    background: var(--backdrop);
    font-family: "Barlow", Arial, sans-serif;
  }
  .stage {
    position: relative;
    width: 1200px;
    height: 900px;
  }
  .card {
    position: absolute;
    box-sizing: border-box;
  }
  .card--front {
    left: 229px;
    top: 115px;
    width: 289px;
    height: 522px;
    background: var(--card-white);
  }
  .card--back {
    left: 622px;
    top: 237px;
    width: 290px;
    height: 523px;
    background: var(--card-black);
    color: var(--light-text);
  }
  .brand-mark {
    position: absolute;
    left: 0;
    right: 0;
    display: flex;
    align-items: center;
    justify-content: center;
    gap: 9px;
    font-weight: 400;
    white-space: nowrap;
  }
  .card--front .brand-mark {
    top: 150px;
    font-size: 30px;
    color: var(--ink);
    letter-spacing: 0.5px;
  }
  .brand-dot {
    width: 14px;
    height: 14px;
    border-radius: 50%;
    background: var(--brand-red);
    flex: none;
  }
  .website {
    position: absolute;
    left: 0;
    right: 0;
    top: 452px;
    text-align: center;
    font-size: 15px;
    font-weight: 300;
    color: var(--ink);
  }
  .website strong { font-weight: 500; }
  .contact {
    position: absolute;
    left: 17px;
    top: 48px;
    font-weight: 300;
    font-size: 15.5px;
    line-height: 20px;
  }
  .contact-name {
    margin: 0 0 0 23px;
    font-size: 22px;
    line-height: 26px;
    font-weight: 400;
    color: var(--brand-red);
  }
  .contact-role {
    margin: 0 0 14px 23px;
    font-size: 15.5px;
    letter-spacing: 0.3px;
  }
  .contact-row {
    display: flex;
    margin: 0;
  }
  .contact-row + .contact-group { margin-top: 18px; }
  .contact-label {
    width: 23px;
    flex: none;
    color: var(--brand-red);
  }
  .card--back .brand-mark {
    top: 426px;
    font-size: 23px;
    color: var(--light-text);
    letter-spacing: 1.5px;
    text-transform: uppercase;
    gap: 8px;
  }
  .card--back .brand-dot { width: 10px; height: 10px; }
</style>
</head>
<body>
<main class="stage">
  <section class="card card--front">
    <div class="brand-mark"><span class="brand-dot"></span>Lorin Studios</div>
    <p class="website">www.<strong>lorin-studios</strong>.com</p>
  </section>

  <section class="card card--back">
    <div class="contact">
      <h1 class="contact-name">Lorin Tay</h1>
      <p class="contact-role">DIRECTOR</p>
      <div class="contact-group">
        <p class="contact-row"><span class="contact-label">A</span><span>Postal Po Box 218</span></p>
        <p class="contact-row"><span class="contact-label"></span><span>Harbour Vale 4821</span></p>
        <p class="contact-row"><span class="contact-label"></span><span>Unit 3 14-16 Ashcombe Rd</span></p>
        <p class="contact-row"><span class="contact-label"></span><span>Harbour Vale 4821</span></p>
      </div>
      <div class="contact-group" style="margin-top:18px">
        <p class="contact-row"><span class="contact-label">M</span><span>0400 555 012</span></p>
        <p class="contact-row"><span class="contact-label">E</span><span>ltay@lorin-studios.com</span></p>
      </div>
    </div>
    <div class="brand-mark"><span class="brand-dot"></span>Lorin Studios</div>
  </section>
</main>
</body>
</html>
```